Tarvo Staffing
Business Card Design
Project: Tarvo Staffing
Tarvo Staffing  -
Creative Brief
Simple
Dov Marsh
Director / Principal Consultant
Suite 1400 7100 Brookhaven Lane Charlotte, NC 28217
dov.marsh@tarvostaffing.com
tarvostaffing.com
please also include: linkedin.com/in/dovmarsh7316
please use the green 'e' icon with the leaf from the logo - perhaps on a gray background; might include the website again on the back if it looks good.

```html
<!DOCTYPE html>
<html lang="en">
<head>
<meta charset="utf-8">
<title>Tarvo Staffing – Stationery Set</title>
<link href="https://fonts.googleapis.com/css2?family=Questrial&display=swap" rel="stylesheet">
<style>
  :root {
    --canvas: #e8e6e2;
    --green: #4f9a1c;
    --green-light: #8cc63f;
    --gray: #9a9a9a;
    --gray-light: #c9c9c9;
    --paper: #ffffff;
    --paper-shade: #f1f3f0;
    --ink: #3a3a3a;
    --ink-soft: #7d7d7d;
  }
  * { box-sizing: border-box; margin: 0; padding: 0; }
  html, body { width: 1200px; height: 660px; overflow: hidden; }
  body {
    background: var(--canvas);
    font-family: "Questrial", "Century Gothic", sans-serif;
    color: var(--ink);
    position: relative;
  }
  .piece { position: absolute; box-shadow: 0 4px 10px rgba(0,0,0,.18); }
  .brand { display: flex; align-items: center; gap: 6px; white-space: nowrap; }
  .brand-dot { flex: none; border-radius: 50%; background: var(--green); }
  .brand-name { color: var(--green); line-height: 1; }

  /* business card backs */
  .card { left: 113px; width: 223px; height: 127px; border-radius: 6px; overflow: hidden; }
  .card-back-green { top: 120px; background: radial-gradient(circle at 70% 40%, var(--green-light), var(--green) 70%); }
  .card-back-white { top: 276px; background: linear-gradient(135deg, var(--paper), var(--paper-shade)); }
  .card-back-gray  { top: 428px; background: radial-gradient(circle at 40% 40%, #bcbcbc, var(--gray) 75%); }
  .card-mark {
    position: absolute; left: 10px; top: 18px;
    width: 84px; height: 84px; border-radius: 50%;
    background: rgba(255,255,255,.22);
  }
  .card-back-white .card-mark { background: rgba(79,154,28,.12); }
  .card-url { position: absolute; right: 14px; bottom: 12px; font-size: 8px; color: #fff; }
  .card-back-white .card-url { color: var(--green); }

  /* letterhead */
  .letterhead-under { left: 384px; top: 124px; width: 324px; height: 484px; background: var(--paper); }
  .letterhead { left: 372px; top: 113px; width: 324px; height: 484px; background: var(--paper); }
  .lh-band { position: absolute; left: 0; right: 0; top: 0; height: 26px;
    background: linear-gradient(90deg, var(--green-light), var(--green)); }
  .lh-brand { position: absolute; left: 14px; top: 36px; }
  .lh-brand .brand-dot { width: 12px; height: 12px; }
  .lh-brand .brand-name { font-size: 18px; }
  .lh-contact { position: absolute; top: 34px; font-size: 5px; line-height: 7px; color: var(--ink-soft); }
  .lh-contact.mid { left: 184px; }
  .lh-contact.end { left: 258px; }
  .lh-watermark {
    position: absolute; left: 46px; top: 128px; width: 220px; height: 220px;
    border-radius: 50%; background: var(--paper-shade);
  }

  /* envelope backs */
  .envelope-back { left: 737px; width: 295px; height: 108px; background: var(--paper); overflow: hidden; }
  .envelope-back svg { position: absolute; inset: 0; }
  .env-gray  { top: 113px; }
  .env-green { top: 238px; }
  .env-white { top: 352px; }
  .flap-mark { position: absolute; left: 139px; top: 36px; width: 18px; height: 18px; border-radius: 50%; }

  /* envelope front */
  .envelope-front { left: 780px; top: 372px; width: 276px; height: 120px; background: var(--paper); }
  .ef-band { position: absolute; left: 0; right: 0; top: 0; height: 22px;
    background: linear-gradient(90deg, var(--green-light), var(--green)); }
  .ef-brand { position: absolute; left: 14px; top: 30px; }
  .ef-brand .brand-dot { width: 9px; height: 9px; }
  .ef-brand .brand-name { font-size: 11px; }
  .ef-address { position: absolute; left: 14px; top: 50px; font-size: 5px; line-height: 7px; color: var(--ink-soft); }

  /* business card front */
  .card-front { left: 648px; top: 456px; width: 245px; height: 132px; background: var(--paper); border-radius: 6px; overflow: hidden; }
  .cf-band { position: absolute; left: 0; right: 0; top: 0; height: 22px;
    background: linear-gradient(90deg, var(--green-light), var(--green)); }
  .cf-brand { position: absolute; left: 10px; top: 58px; }
  .cf-brand .brand-dot { width: 10px; height: 10px; }
  .cf-brand .brand-name { font-size: 14px; }
  .cf-details { position: absolute; left: 146px; top: 32px; font-size: 5px; line-height: 7px; color: var(--ink-soft); }
  .cf-name { font-size: 7px; line-height: 9px; color: var(--ink); }
  .cf-url { position: absolute; left: 10px; bottom: 8px; font-size: 5px; color: var(--green); }
</style>
</head>
<body>

  <div class="piece card card-back-green">
    <div class="card-mark"></div>
    <span class="card-url">tarvostaffing.com</span>
  </div>
  <div class="piece card card-back-white">
    <div class="card-mark"></div>
    <span class="card-url">tarvostaffing.com</span>
  </div>
  <div class="piece card card-back-gray">
    <div class="card-mark"></div>
    <span class="card-url">tarvostaffing.com</span>
  </div>

  <div class="piece letterhead-under"></div>
  <div class="piece letterhead">
    <div class="lh-band"></div>
    <div class="brand lh-brand"><span class="brand-dot"></span><span class="brand-name">Tarvo Staffing</span></div>
    <div class="lh-contact mid">Dov Marsh<br>Street Address<br>City, State ZIP</div>
    <div class="lh-contact end">Phone Number<br>Email Address<br>Website</div>
    <div class="lh-watermark"></div>
  </div>

  <div class="piece envelope-back env-gray">
    <svg width="295" height="108" viewBox="0 0 295 108"><polygon points="0,0 295,0 147,68" fill="var(--gray-light)"/><polyline points="0,108 147,56 295,108" fill="none" stroke="#e3e3e3"/></svg>
    <span class="flap-mark" style="background:#fff"></span>
  </div>
  <div class="piece envelope-back env-green">
    <svg width="295" height="108" viewBox="0 0 295 108"><polygon points="0,0 295,0 147,68" fill="var(--green)"/><polyline points="0,108 147,56 295,108" fill="none" stroke="#e3e3e3"/></svg>
    <span class="flap-mark" style="background:#fff"></span>
  </div>
  <div class="piece envelope-back env-white">
    <svg width="295" height="108" viewBox="0 0 295 108"><polygon points="0,0 295,0 147,68" fill="#f7f7f7" stroke="#dcdcdc"/><polyline points="0,108 147,56 295,108" fill="none" stroke="#e3e3e3"/></svg>
    <span class="flap-mark" style="background:var(--green)"></span>
  </div>

  <div class="piece envelope-front">
    <div class="ef-band"></div>
    <div class="brand ef-brand"><span class="brand-dot"></span><span class="brand-name">Tarvo Staffing</span></div>
    <div class="ef-address">Dov Marsh<br>Street Address<br>City, State ZIP</div>
  </div>

  <div class="piece card-front">
    <div class="cf-band"></div>
    <div class="brand cf-brand"><span class="brand-dot"></span><span class="brand-name">Tarvo Staffing</span></div>
    <div class="cf-details">
      <div class="cf-name">Dov Marsh</div>
      Director / Principal Consultant<br>
      Street Address<br>
      City, State ZIP<br>
      Email Address<br>
      Profile Link
    </div>
    <span class="cf-url">tarvostaffing.com</span>
  </div>

</body>
</html>
```